Marlowick APP redesign and color change

I am looking for a new design for my app. Please see the attached current design.

Currently, I have a functioning app but the colors and design are awful!
The logo is great but the rest of the app needs a refresh.
(Logo hi res not yet available but will upload soon.)
New colors or anything that is cutting edge.

Basically: It is a secure social media app within a school system where the teachers, students and parents can text, exchange photos, plan curriculum, etc.

I NEED ONLY landing page with a new look!
Looking for one distinct design for the landing page with new look.
The developer will apply this one design towards the rest of the pages/app screens.

Because part of the social media I need the feel and look of what is now the trend. Something that will attract and keep the client(s) interested. I am really leaving all the creative work to the designer and open to any suggestions.
Updates

Target Market(s)

Schools, community, teachers, students, colleges, sport teams

Industry/Entity Type

Non Profit

Font styles to use
Serif
Sans Serif

Colors

Designer to choose colors to be used in the design.

Requirements
Must have
• Sharp, trendy, millennial feel
Nice to have
• Up to designer
Should not have
• Up to designer

```html
<!DOCTYPE html>
<html lang="en">
<head>
<meta charset="utf-8">
<title>Marlowick — App Onboarding Screens</title>
<link rel="stylesheet" href="https://fonts.googleapis.com/css2?family=Fira+Sans:wght@400;500&family=Roboto:wght@400;500&display=swap">
<style>
  :root {
    --stage-top: #252525;
    --stage-bottom: #4a4a4a;
    --screen-bg: #f7f7f7;
    --field-bg: #ffffff;
    --field-border: #e6e6e6;
    --ink: #222222;
    --ink-soft: #3a3a3a;
    --placeholder: #9a9a9a;
    --teal: #3bbf9f;
    --blue: #2470a0;
    --brand: #2a8f9a;
    --link: #2a9fb4;
    --outline: #2c6f9a;
    --grad: linear-gradient(90deg, var(--teal) 0%, var(--blue) 100%);
  }
  * { box-sizing: border-box; margin: 0; padding: 0; }
  html, body { width: 1200px; height: 800px; overflow: hidden; }
  body {
    background: linear-gradient(180deg, var(--stage-top) 0%, var(--stage-bottom) 100%);
    font-family: "Fira Sans", sans-serif;
    color: var(--ink);
    position: relative;
  }
  .screen {
    position: absolute;
    background: var(--screen-bg);
    height: 608px;
  }
  .screen--welcome { left: 46px; top: 130px; width: 344px; }
  .screen--signup  { left: 426px; top: 132px; width: 340px; }
  .screen--signin  { left: 802px; top: 130px; width: 342px; }

  .status-bar {
    position: absolute; left: 0; right: 0; top: 3px; height: 14px;
    font-family: "Roboto", sans-serif; font-size: 11px; color: #111;
    display: flex; align-items: center; justify-content: space-between;
    padding: 0 6px;
  }
  .status-bar__carrier { display: flex; align-items: center; gap: 3px; }
  .status-bar__time { position: absolute; left: 50%; transform: translateX(-50%); font-weight: 500; }
  .status-bar__battery { display: flex; align-items: center; gap: 4px; }
  .battery {
    width: 20px; height: 9px; border: 1px solid #111; border-radius: 2px; position: relative;
  }
  .battery::before { content: ""; position: absolute; left: 1px; top: 1px; bottom: 1px; width: 4px; background: #111; }
  .battery::after { content: ""; position: absolute; right: -3px; top: 2px; width: 2px; height: 3px; background: #111; }

  .brand-name {
    position: absolute; left: 0; right: 0; top: 100px; text-align: center;
    font-size: 26px; font-weight: 500; letter-spacing: 0; color: var(--brand);
  }
  .tagline {
    position: absolute; left: 0; right: 0; top: 136px; text-align: center;
    font-size: 12.5px; font-weight: 400; letter-spacing: 0.5px; color: var(--ink-soft);
  }
  .welcome__prompt {
    position: absolute; left: 0; right: 0; top: 502px; text-align: center;
    font-size: 14.5px; letter-spacing: 0.6px; color: var(--ink-soft);
  }
  .btn {
    position: absolute; display: flex; align-items: center; justify-content: center;
    font-family: "Fira Sans", sans-serif; font-weight: 400; letter-spacing: 0.5px;
  }
  .btn--primary { background: var(--grad); color: #fff; box-shadow: 0 6px 10px rgba(0,0,0,0.18); }
  .btn--outline { border: 2px solid var(--outline); color: var(--outline); background: transparent; }
  .btn--start { left: 26px; top: 535px; width: 132px; height: 48px; font-size: 16px; }
  .btn--signin-outline { left: 186px; top: 535px; width: 132px; height: 48px; font-size: 16px; }

  .heading {
    position: absolute; left: 0; right: 0; text-align: center;
    font-size: 15px; font-weight: 400; letter-spacing: 0.8px; color: var(--ink-soft); line-height: 22px;
  }
  .heading strong { font-weight: 500; font-size: 17px; color: var(--ink); }
  .screen--signup .heading { top: 100px; }
  .screen--signin .heading { top: 124px; }

  .field {
    position: absolute; left: 34px; width: 272px; height: 54px;
    background: var(--field-bg); border: 1px solid var(--field-border); border-radius: 2px;
    display: flex; align-items: center; padding-left: 22px;
    font-size: 13.5px; color: var(--placeholder); letter-spacing: 0.3px;
  }
  .screen--signin .field { width: 273px; }

  .check-row {
    position: absolute; left: 34px; right: 34px; display: flex; align-items: center;
    font-size: 11px; color: var(--ink);
  }
  .check {
    width: 18px; height: 18px; border-radius: 50%; background: #fff;
    box-shadow: 0 1px 3px rgba(0,0,0,0.15); display: flex; align-items: center; justify-content: center;
    margin-right: 11px;
  }
  .check-row__end { margin-left: auto; }

  .btn--submit { left: 35px; width: 273px; height: 55px; font-size: 17px; border-radius: 2px; }
  .screen--signup .btn--submit { top: 430px; width: 272px; }
  .screen--signin .btn--submit { top: 384px; height: 54px; }

  .footnote {
    position: absolute; left: 0; right: 0; text-align: center; font-size: 10.5px; color: var(--ink);
  }
  .footnote a { color: var(--link); text-decoration: none; }
</style>
</head>
<body>

  <section class="screen screen--welcome">
    <div class="status-bar">
      <span class="status-bar__carrier">●●●○○ KESTREL
        <svg width="11" height="8" viewBox="0 0 11 8"><path d="M1 3a6 6 0 0 1 9 0M2.8 4.8a3.5 3.5 0 0 1 5.4 0M5.5 7.5l-1.2-1.3a1.7 1.7 0 0 1 2.4 0z" fill="none" stroke="#111" stroke-width="1.2"/></svg>
      </span>
      <span class="status-bar__time">4:21 PM</span>
      <span class="status-bar__battery">✱ 22% <span class="battery"></span></span>
    </div>
    <div class="brand-name">Marlowick</div>
    <div class="tagline">Safe spaces for every school</div>
    <p class="welcome__prompt">Create a new account or sign in</p>
    <a class="btn btn--primary btn--start">Get Started</a>
    <a class="btn btn--outline btn--signin-outline">Sign In</a>
  </section>

  <section class="screen screen--signup">
    <div class="status-bar">
      <span class="status-bar__carrier">●●●○○ KESTREL
        <svg width="11" height="8" viewBox="0 0 11 8"><path d="M1 3a6 6 0 0 1 9 0M2.8 4.8a3.5 3.5 0 0 1 5.4 0M5.5 7.5l-1.2-1.3a1.7 1.7 0 0 1 2.4 0z" fill="none" stroke="#111" stroke-width="1.2"/></svg>
      </span>
      <span class="status-bar__time">4:21 PM</span>
      <span class="status-bar__battery">✱ 22% <span class="battery"></span></span>
    </div>
    <h2 class="heading">You are New Here<br>Please <strong>Sign Up</strong></h2>
    <div class="field" style="top:162px">Username</div>
    <div class="field" style="top:230px">Password</div>
    <div class="field" style="top:298px">Confirm Password</div>
    <div class="check-row" style="top:375px">
      <span class="check"><svg width="9" height="8" viewBox="0 0 9 8"><path d="M1 4l2.4 2.5L8 1.2" fill="none" stroke="#111" stroke-width="1.8"/></svg></span>
      Accept Terms &amp; Conditions
    </div>
    <a class="btn btn--primary btn--submit">Sign Up Now</a>
    <p class="footnote" style="top:508px">Already have an account? <a>Sign up</a></p>
  </section>

  <section class="screen screen--signin">
    <div class="status-bar">
      <span class="status-bar__carrier">●●●○○ KESTREL
        <svg width="11" height="8" viewBox="0 0 11 8"><path d="M1 3a6 6 0 0 1 9 0M2.8 4.8a3.5 3.5 0 0 1 5.4 0M5.5 7.5l-1.2-1.3a1.7 1.7 0 0 1 2.4 0z" fill="none" stroke="#111" stroke-width="1.2"/></svg>
      </span>
      <span class="status-bar__time">4:21 PM</span>
      <span class="status-bar__battery">✱ 22% <span class="battery"></span></span>
    </div>
    <h2 class="heading">You are just One Step<br>Go To <strong>Sign In</strong></h2>
    <div class="field" style="top:188px">Username</div>
    <div class="field" style="top:256px">Password</div>
    <div class="check-row" style="top:329px">
      <span class="check"><svg width="9" height="8" viewBox="0 0 9 8"><path d="M1 4l2.4 2.5L8 1.2" fill="none" stroke="#111" stroke-width="1.8"/></svg></span>
      Remember me
      <span class="check-row__end">Fogot Password?</span>
    </div>
    <a class="btn btn--primary btn--submit">Sign In</a>
    <p class="footnote" style="top:472px">Create a account? <a>Sign up</a></p>
  </section>

</body>
</html>
```